Report template for evaluation reports to be used by non designers

We are looking for a report template that meets all the requirements listed in the attached documents. letter head, logo etc have been enclosed. Its important that the colour integrity is kept, but beyond that options are welcome.
Its important that the document is extremely easy to use and that is able to be adapted to include eatables, figures, pictures, text boxes etc and keep the integrity of the template

Target Market(s)

Governments, Civil society organisations and research institutions

Font styles to use
Sans Serif

Colors
6b449b
876aae
c0c0c0
000000

Requirements
Must have
• Clean, professional, not concluded, modern, must be easy to use
Should not have
• too busy, hard to use

```html
<!DOCTYPE html>
<html lang="en">
<head>
<meta charset="utf-8">
<title>Orvelin Research Institute – Report Template</title>
<link href="https://fonts.googleapis.com/css2?family=Open+Sans:wght@400;600;700&display=swap" rel="stylesheet">
<style>
  :root{
    --stage:#d6d6d6;
    --cover:#4a3b96;
    --cover-accent:#7b6fc2;
    --brand:#4a3b96;
    --paper:#ffffff;
    --ink:#1c1c1c;
    --muted:#6a6a6a;
    --white:#ffffff;
  }
  *{margin:0;padding:0;box-sizing:border-box}
  html,body{width:1200px;height:783px;overflow:hidden;background:var(--stage);font-family:"Open Sans",Arial,sans-serif}
  .canvas{position:relative;width:1200px;height:783px}

  /* Cover page */
  .cover{position:absolute;left:43px;top:44px;width:548px;height:708px;background:var(--cover);color:var(--white);overflow:hidden}
  .cover__logo{position:absolute;left:46px;top:58px;display:flex;align-items:center;gap:12px}
  .cover__logo-dot{width:22px;height:22px;border-radius:50%;background:var(--cover-accent)}
  .cover__logo-name{font-size:38px;font-weight:400;letter-spacing:7px;color:var(--white)}
  .cover__bar{position:absolute;left:26px;top:302px;width:27px;height:178px;background:var(--cover-accent)}
  .cover__title{position:absolute;left:75px;top:292px;font-size:45px;font-weight:700;line-height:52px;letter-spacing:.3px;white-space:nowrap}
  .cover__client{position:absolute;left:75px;top:452px;font-size:22px;font-weight:400;letter-spacing:.3px}
  .cover__contact{position:absolute;left:0;right:0;top:640px;text-align:center;font-size:11.5px;white-space:nowrap}
  .cover__web{position:absolute;left:0;right:0;top:662px;height:12px;display:flex;align-items:center}
  .cover__web-line{flex:1;height:8px;background:var(--cover-accent)}
  .cover__web-text{padding:0 6px;font-size:10.5px;letter-spacing:4.3px;color:var(--white);line-height:12px}

  /* Inner page */
  .page{position:absolute;left:615px;top:44px;width:546px;height:708px;background:var(--paper);color:var(--ink);overflow:hidden}
  .page__rule{position:absolute;left:0;right:0;top:35px;height:1.5px;background:var(--brand)}
  .page__logo{position:absolute;right:40px;top:22px;padding:0 6px;background:var(--paper);display:flex;align-items:center;gap:6px}
  .page__logo-dot{width:9px;height:9px;border-radius:50%;background:var(--brand)}
  .page__logo-name{font-size:18px;font-weight:400;letter-spacing:3px;color:var(--brand);line-height:24px}
  .page__heading{position:absolute;left:62px;top:78px;font-size:33px;font-weight:400;color:var(--brand);letter-spacing:.2px;white-space:nowrap}
  .page__heading-rule{position:absolute;left:62px;top:120px;width:438px;height:3px;background:var(--brand)}
  .summary{position:absolute;left:57px;top:154px;width:449px;height:520px;column-count:2;column-gap:27px;column-fill:auto;font-size:9.7px;line-height:14.4px;text-align:justify;color:var(--ink)}
  .summary p{margin-bottom:11px}
  .summary__mark{padding-right:26px}

  .page__footer{position:absolute;left:0;right:0;top:677px;height:16px;display:flex;align-items:center}
  .page__footer-url{flex:none;background:var(--brand);color:var(--white);font-size:10px;letter-spacing:.5px;height:16px;line-height:16px;padding:0 12px 0 14px;width:180px;white-space:nowrap;clip-path:polygon(0 0,100% 0,calc(100% - 8px) 100%,0 100%)}
  .page__footer-topics{flex:1;min-width:0;position:relative;font-size:9.3px;color:var(--muted);padding-left:6px;height:16px;line-height:16px;white-space:nowrap;overflow:hidden;word-spacing:1px}
  .page__footer-topics::after{content:"";position:absolute;left:0;right:0;bottom:0;height:1px;background:var(--brand)}
  .page__footer-number{flex:none;font-size:10.5px;color:var(--ink);padding:0 6px;height:16px;line-height:16px;position:relative}
  .page__footer-number::after{content:"";position:absolute;left:0;right:0;bottom:0;height:1px;background:var(--brand)}
  .page__footer-tab{flex:none;width:24px;height:16px;background:var(--brand);clip-path:polygon(8px 0,100% 0,100% 100%,0 100%)}
</style>
</head>
<body>
<div class="canvas">

  <section class="cover">
    <div class="cover__logo">
      <span class="cover__logo-dot"></span>
      <span class="cover__logo-name">ORVELIN</span>
    </div>
    <div class="cover__bar"></div>
    <h1 class="cover__title">ORVELIN RESEARCH<br>INSTITUTE (ORI)<br>REPORTING</h1>
    <p class="cover__client">CLIENT NAME 15-06-2018</p>
    <p class="cover__contact">+41 700 000 000 | info@orvelinresearch.org | Registration Number: CHF-000.000.000</p>
    <div class="cover__web">
      <span class="cover__web-line"></span>
      <span class="cover__web-text">www.orvelinresearch.org</span>
      <span class="cover__web-line"></span>
    </div>
  </section>

  <section class="page">
    <div class="page__rule"></div>
    <div class="page__logo">
      <span class="page__logo-dot"></span>
      <span class="page__logo-name">ORVELIN</span>
    </div>
    <h2 class="page__heading">EXECUTIVE SUMMARY</h2>
    <div class="page__heading-rule"></div>

    <div class="summary">
      <p><span class="summary__mark">o</span>The Institute is an independent research centre set up to improve the understanding of national public policies and to promote the adoption of new approaches in programme design. In addition, the Institute aims to shed more light on the role of social and regional development in the broader development pathway of a country.[6][7][8][9] The mission of the Institute is to provide evidence-based policy solutions that sustainably reduce poverty and strengthen public services.[10]</p>
      <p>The Institute carries out policy research and shares it through a wide range of publications, bulletins, conferences, and other initiatives. Each evaluation follows a clear method agreed with the client, and findings are reviewed by an independent panel before they are released.[11][12] The Institute works with partners in many regions, and its research staff support teams in the field. Most of the work takes place alongside governments, civil society organisations and research institutions.</p>
      <p>The Institute is part of a network of research centres funded in part by a partner consortium,[13] which in turn is supported by governments, private businesses and foundations, and multilateral lenders.[14][15][16][17] <span class="summary__mark">o</span>The Institute is an independent research centre set up to improve the understanding of national public policies and to promote the adoption of new approaches in programme design. In addition, the Institute aims to shed more light on the role of social and regional development in the broader development pathway of a country.[6][7][8][9] The mission of the Institute is to provide evidence-based policy solutions that sustainably reduce poverty and strengthen public services.[10]</p>
      <p>The Institute carries out policy research and shares it through a wide range of publications, bulletins, conferences, and other initiatives. Each evaluation follows a clear method agreed with the client, and findings are reviewed by an independent panel before they are released.[11][12] The Institute works with partners in many regions, and its research staff support teams in the field. Most of the work takes place alongside governments, civil society organisations and research institutions.</p>
      <p>The Institute is part of a network of research centres funded in part by a partner consortium,[13] which in turn is supported by governments, private businesses and foundations, and multilateral lenders.[14][15][16][17]</p>
    </div>

    <div class="page__footer">
      <span class="page__footer-url">www.orvelinresearch.org</span>
      <span class="page__footer-topics">evaluation&nbsp; research&nbsp; policy analysis&nbsp; capacity development&nbsp; training</span>
      <span class="page__footer-number">01</span>
      <span class="page__footer-tab"></span>
    </div>
  </section>

</div>
</body>
</html>
```